Wordpress theme for food/recipe blog - family friendly

I've recently setup a Wordpress site to document all my tried and tested recipes. However I'm not happy with the design and layout of the theme I got. See sunnyoventable.com

It's also lacking a header/identity/logo as well. I would like a theme which is eye catching, cute and easy to navigate bearing in mind that the site is meant to be a personal blog documenting my culinary journey.

I would definitely like a logo / cartoon of a chubby, dimpled specky girl in apron perhaps holding up some utensil to show what this blog is about. I cook mainly for my family comprising my husband and our little baby girl who is 16months.

I love making breads the most if that helps with the logo/header design.
Updates

Reason: need more designs

Target Market(s)

- family with young kids
- mummies
- amateur cooks
- people who love food/ baking and cooking and sharing recipes

Industry/Entity Type

Baby

Requirements
Must have
• - Viewable on mobile - ie must be mobile friendly
- header/image - when shared on social media the image will be the one that is identified by people/readers

```html
<!DOCTYPE html>
<html lang="en">
<head>
<meta charset="utf-8">
<title>Sunny oven table – Spoonful of love</title>
<link rel="stylesheet" href="https://fonts.googleapis.com/css2?family=Source+Sans+3:wght@400;600&family=Arimo:wght@400&display=swap">
<style>
  :root {
    --brown-bar: #4f3d3d;
    --brown-text: #5a4040;
    --ink: #222222;
    --muted: #555555;
    --leaf: #8cbd2e;
    --leaf-box: #93c43a;
    --berry: #c21f2b;
    --link: #b3202a;
    --rule: #bdbdbd;
    --footer: #4f4f4f;
    --footer-base: #3a3a3a;
    --paper: #ffffff;
  }
  * { box-sizing: border-box; margin: 0; padding: 0; }
  html, body { width: 868px; height: 1200px; overflow: hidden; background: var(--paper); }
  body { position: relative; font-family: "Source Sans 3", sans-serif; color: var(--ink); }
  .abs { position: absolute; }

  .welcome-bar { left: 0; top: 0; width: 868px; height: 27px; background: var(--brown-bar); }
  .welcome-bar span { position: absolute; left: 105px; top: 6px; color: #fff; font: 13px "Arimo", sans-serif; }

  .brand-mark { left: 104px; top: 38px; width: 56px; height: 56px; border-radius: 50%; background: var(--berry); }
  .brand-name { left: 117px; top: 96px; font-size: 35px; color: var(--brown-text); letter-spacing: -0.3px; }
  .brand-tagline { left: 117px; top: 134px; font-size: 17px; color: var(--leaf); }
  .intro-box { left: 116px; top: 156px; width: 297px; height: 110px; background: var(--leaf-box); padding: 10px 12px; color: #2d2d2d; font-size: 11.5px; line-height: 14px; }
  .header-photo { left: 416px; top: 27px; width: 352px; height: 255px; background: linear-gradient(135deg, #f3e6d6 0%, #d9a86a 40%, #c2403a 75%, #6a8a3a 100%); }

  .main-nav { left: 0; top: 282px; width: 868px; height: 34px; background: var(--berry); }
  .main-nav ul { list-style: none; display: flex; position: absolute; left: 105px; top: 0; height: 34px; }
  .main-nav li { height: 34px; display: flex; align-items: center; padding: 0 18px 0 19px; border-right: 1px solid #9e1822; color: #fff; font: 11px "Arimo", sans-serif; }
  .main-nav li.current { padding: 0; border-right: 1px solid #9e1822; }
  .main-nav li.current span { background: var(--leaf); height: 26px; display: flex; align-items: center; padding: 0 11px; margin-right: 13px; color: #fff; }

  .post-title { left: 98px; font-size: 20px; color: #3b2e2e; }
  .post-date { left: 100px; font-size: 8px; color: var(--muted); }
  .post-photo { left: 100px; width: 426px; height: 194px; }
  .post-excerpt { left: 100px; width: 428px; font-size: 9.6px; line-height: 12.5px; color: var(--ink); }
  .learn-more { font-size: 8.5px; color: var(--link); text-decoration: underline; }
  .post-rule { left: 100px; width: 414px; border-top: 1px dotted #d8d8d8; }

  .sidebar-rule { left: 583px; width: 184px; border-top: 1px dotted #888; }
  .search-field { left: 583px; top: 348px; width: 140px; height: 23px; border: 1px solid #444; font-size: 9px; padding: 6px 8px; color: #555; }
  .search-button { left: 727px; top: 348px; width: 40px; height: 23px; background: #333; color: #fff; font: 9px "Arimo", sans-serif; display: flex; align-items: center; justify-content: center; }
  .follow-label { left: 587px; top: 430px; font-size: 11px; color: var(--leaf); }
  .social-dot { top: 424px; width: 26px; height: 26px; border-radius: 50%; background: #333; }
  .widget-title { left: 587px; font-size: 19px; color: #3b2e2e; }
  .about-photo { left: 585px; top: 516px; width: 148px; height: 99px; border: 1px solid #d0d0d0; padding: 4px; }
  .about-photo div { width: 100%; height: 100%; background: #dcdcdc; }
  .about-text { left: 587px; top: 624px; width: 150px; font-size: 8.6px; line-height: 10.5px; color: var(--muted); }
  .category-list { left: 590px; top: 760px; list-style: none; }
  .category-list li { height: 28px; font-size: 12px; color: #333; display: flex; align-items: center; gap: 12px; }
  .category-list svg { width: 5px; height: 7px; }

  .site-footer { left: 0; top: 1064px; width: 868px; height: 46px; background: var(--footer); }
  .site-footer nav { position: absolute; left: 0; width: 100%; top: 16px; text-align: center; color: #fff; font: 10px "Arimo", sans-serif; word-spacing: 2px; }
  .site-footer nav b { font-weight: 400; margin: 0 17px; }
  .footer-base { left: 0; top: 1110px; width: 868px; height: 22px; background: var(--footer-base); color: #bbb; font: 8px "Arimo", sans-serif; text-align: center; padding-top: 7px; }
</style>
</head>
<body>
  <div class="abs welcome-bar"><span>Welcome to my website!</span></div>

  <div class="abs brand-mark"></div>
  <div class="abs brand-name">Sunny oven table</div>
  <div class="abs brand-tagline">Spoonful of love ...</div>
  <p class="abs intro-box">This blog is an attempt to document all my recipes (tried and tested of course). I'm starting to realize that I'm very forgetful as I age and sometimes I lack inspiration which results in me surfing endlessly for something to cook when I know very well, I have a whole recipe bank stashed all over the place!</p>
  <div class="abs header-photo" role="img" aria-label="Header photo collage: a toddler snacking, a basket of fresh breads, a noodle dish and fresh raspberries"></div>

  <nav class="abs main-nav">
    <ul>
      <li class="current"><span>HOME</span></li>
      <li>ABOUT</li>
      <li>BLOG</li>
      <li>SERVICES</li>
      <li>CONTACT ME</li>
    </ul>
  </nav>

  <h2 class="abs post-title" style="top:340px">Chestnut Chicken Stew with Carrots and Potatoes</h2>
  <div class="abs post-date" style="top:366px">September 23, 2013</div>
  <div class="abs post-photo" style="top:386px; background: linear-gradient(160deg, #5a3a2c 0%, #8a4a3a 45%, #3e2a22 80%, #6e7a4a 100%);" role="img" aria-label="Photo of chestnut chicken stew with carrots and potatoes"></div>
  <p class="abs post-excerpt" style="top:591px">While shopping for my fish pie ingredients, I saw one of the vegetables seller selling Chestnuts! I planned to make Chicken Stew too so I thought, why not add Chestnuts since I love eating roast chestnuts and I'm sure the flavour would go really well with the stew. I turned to my husband and asked [...]</p>
  <a class="abs learn-more" style="left:100px; top:647px">Learn more</a>
  <div class="abs post-rule" style="top:683px"></div>

  <h2 class="abs post-title" style="top:696px">Plump Claw Recipe</h2>
  <div class="abs post-date" style="top:722px">September 24, 2013</div>
  <div class="abs post-photo" style="top:756px; background: linear-gradient(120deg, #efe0c0 0%, #e9cfa0 25%, #b4582e 50%, #7a5236 80%, #e8e4e0 100%);" role="img" aria-label="Photo of crab in a rich sauce served with slices of bread"></div>
  <p class="abs post-excerpt" style="top:962px">I love crabs but I can't eat them too often as it's too indulgent. My favourite has got to be salted egg yolk, black pepper and Plump Claw's version. I'm not a big fan of the Singapore version as I find it too sweet half the time. The mere mention of Plump Claw, to those [...]</p>
  <a class="abs learn-more" style="left:100px; top:1011px">Learn more</a>

  <div class="abs search-field">text here ..................</div>
  <div class="abs search-button">Search</div>
  <div class="abs sidebar-rule" style="top:402px"></div>
  <div class="abs follow-label">Follow me:</div>
  <div class="abs social-dot" style="left:656px"></div>
  <div class="abs social-dot" style="left:685px"></div>
  <div class="abs social-dot" style="left:714px"></div>
  <div class="abs social-dot" style="left:742px"></div>
  <div class="abs sidebar-rule" style="top:471px"></div>

  <h3 class="abs widget-title" style="top:483px">About me:</h3>
  <div class="abs about-photo" role="img" aria-label="Portrait of the blog author"><div></div></div>
  <p class="abs about-text">In non rutrum augue. Phasellus tincidunt ipsum quis libero tincidunt congue. Nam sodales quis magna ut lacinia.</p>
  <a class="abs learn-more" style="left:587px; top:672px">Learn more</a>
  <div class="abs sidebar-rule" style="top:705px"></div>

  <h3 class="abs widget-title" style="top:719px">Categories</h3>
  <ul class="abs category-list">
    <li><svg viewBox="0 0 5 7"><path d="M0 0L5 3.5L0 7Z" fill="#c21f2b"/></svg>Bakes</li>
    <li><svg viewBox="0 0 5 7"><path d="M0 0L5 3.5L0 7Z" fill="#c21f2b"/></svg>Breakfast</li>
    <li><svg viewBox="0 0 5 7"><path d="M0 0L5 3.5L0 7Z" fill="#c21f2b"/></svg>Chinese</li>
    <li><svg viewBox="0 0 5 7"><path d="M0 0L5 3.5L0 7Z" fill="#c21f2b"/></svg>Drinks</li>
    <li><svg viewBox="0 0 5 7"><path d="M0 0L5 3.5L0 7Z" fill="#c21f2b"/></svg>Kids</li>
    <li><svg viewBox="0 0 5 7"><path d="M0 0L5 3.5L0 7Z" fill="#c21f2b"/></svg>Musings</li>
    <li><svg viewBox="0 0 5 7"><path d="M0 0L5 3.5L0 7Z" fill="#c21f2b"/></svg>Western</li>
  </ul>
  <div class="abs sidebar-rule" style="top:966px"></div>
  <h3 class="abs widget-title" style="top:980px; font-size:16px">Tags</h3>
  <div class="abs sidebar-rule" style="top:1020px"></div>

  <footer class="abs site-footer">
    <nav>Home<b>|</b>About<b>|</b>Blog<b>|</b>Services<b>|</b>Contact Me</nav>
  </footer>
  <div class="abs footer-base">Copyright 2013 www.sunnyoventable.com All Rights Reserved.</div>
</body>
</html>
```